Brindle Haulage Heavy Goods Transport web design

I have a client who requires a new web site design.
They are Brindle Haulage in the UK.
They have a current site which needs updating with a fresh look and feel using modern design ideas.
Their current site is brindlehaulage.co.uk
I will use your design to build a new CMS site for them using Django.
I only require the layered PSD files, main page design plus a sub page showing navigation changes and layout changes between pages.
The site needs to have the same sections as the current site plus:
1) Proof of delivery downloads system (customer logs in to access their delivery documents).
2) CMS system will allow them to add pages so the menu system needs to be designed such that it can expand.
3) A contact page with a contact form and a Google map will be used.
4) No flash.
5) Slideshow banners (using JQuery will be used).
I like the following type of designs:
www.billomatic.com/pricing.html
www.tallyleaf.com/
vantor.ly/features
navgridpro.com/
I am looking for a designer to work with me designing other web design projects as well so this project will be used as a test bed for us working together.
The budget for our client designs is between £120 and £200 depending on functionality requirements. This site has a budget of £150.
Please submit your quotes by email to rdalton@norvale.com
Industrial business customers
Build

```html
<!DOCTYPE html>
<html lang="en">
<head>
<meta charset="utf-8">
<title>Brindle Haulage – Road Hauliers and Distribution Specialist</title>
<link rel="stylesheet" href="https://fonts.googleapis.com/css2?family=Ubuntu:wght@400;500;700&family=Arimo:wght@400;700&family=Open+Sans:wght@400;600&display=swap">
<style>
:root{
  --charcoal:#363636;
  --nav-bg:#262626;
  --yellow:#fdbf1f;
  --yellow-text:#fcc118;
  --ink:#333333;
  --paper:#efeeef;
  --paper-top:#e4e4e4;
  --panel:#d3d3d3;
  --white:#ffffff;
  --rule:#a9a9a9;
}
*{box-sizing:border-box;margin:0;padding:0}
html,body{width:1091px;height:1200px;overflow:hidden}
body{position:relative;background:var(--charcoal);font-family:"Arimo",Arial,sans-serif;color:var(--ink)}
.abs{position:absolute}

/* header */
.site-header{left:0;top:0;width:1091px;height:172px;background:linear-gradient(#3a3a3a,#313131)}
.date-badge{left:914px;top:8px;width:120px;height:21px;background:var(--yellow);border-radius:3px;font:700 13px/21px "Arimo",Arial,sans-serif;color:#3a2a00;text-align:center}
.brand{left:38px;top:38px;display:flex;align-items:center;gap:10px;font:700 30px/1 "Ubuntu",sans-serif;color:var(--yellow)}
.brand-mark{width:26px;height:26px;background:var(--yellow)}
.main-nav{left:36px;top:120px;width:1021px;height:46px;background:var(--nav-bg);border:1px solid #4a4a4a;display:flex;align-items:center;padding-left:26px;gap:26px}
.main-nav a{font:500 16px/1 "Ubuntu",sans-serif;color:var(--yellow-text);text-decoration:none;letter-spacing:.3px;white-space:nowrap}
.main-nav a.current{color:var(--white)}

/* hero */
.hero{left:0;top:172px;width:1091px;height:406px;background:var(--yellow)}
.hero-glow{left:698px;top:0;width:372px;height:388px;background:radial-gradient(ellipse at 40% 45%,#fdc320 0%,#f8b21c 70%,#f4a71a 100%)}
.hero-photo{left:38px;top:17px;width:659px;height:347px;border:3px solid #3c3c3c;background:linear-gradient(160deg,#9b9374 0%,#7c7d78 35%,#5e6164 60%,#777a7b 100%);box-shadow:0 18px 18px -12px rgba(0,0,0,.45)}
.slide-dots{left:340px;top:387px;display:flex;gap:5px}
.slide-dots span{width:11px;height:11px;border-radius:50%;background:#333}
.slide-dots span.active{background:#7a5a12}
.hero-title{left:727px;top:36px;font:700 32px/39px "Ubuntu",sans-serif;color:var(--ink);letter-spacing:.6px;text-transform:uppercase;white-space:nowrap}
.hero-services{left:710px;top:193px;width:335px;text-align:center;font:700 21px/26px "Ubuntu",sans-serif;color:var(--ink);letter-spacing:1.2px;text-transform:uppercase}
.hero-slogan{left:710px;top:288px;width:335px;text-align:center;font:700 38px/1 "Ubuntu",sans-serif;color:var(--ink)}

/* content */
.content{left:0;top:578px;width:1091px;height:321px;background:linear-gradient(var(--paper-top),var(--paper) 40%)}
.intro-title{left:38px;top:27px;font:400 21px/1 "Arimo",Arial,sans-serif;color:#222}
.intro-rule{left:38px;top:57px;width:659px;height:1px;background:var(--rule)}
.intro-text{left:38px;top:68px;width:659px;font:400 14.5px/21.8px "Arimo",Arial,sans-serif;color:#2e2e2e;text-align:justify}
.callout{left:55px;top:201px;width:635px;height:86px;background:var(--yellow);border-radius:2px;display:flex;align-items:center;justify-content:center;text-align:center;padding:0 40px;font:700 18px/26px "Ubuntu",sans-serif;color:var(--ink);letter-spacing:.5px}

.login{left:751px;top:22px;width:299px;height:268px}
.login-head{left:0;top:0;width:299px;height:50px;background:linear-gradient(#bdbdbd,#8d8d8d);border-radius:3px 3px 0 0;font:500 18px/50px "Open Sans",sans-serif;color:#222;text-align:center;letter-spacing:.5px}
.login-body{left:6px;top:46px;width:287px;height:222px;background:var(--panel)}
.field-label{left:19px;font:700 15px/1 "Arimo",Arial,sans-serif;color:#222}
.field{left:105px;width:169px;height:31px;background:var(--white);border:1px solid #9c9c9c;border-radius:2px}
.btn{height:35px;background:linear-gradient(#fcc936,#f0a91a);border:1px solid #c98b10;border-radius:3px;font:400 15px/33px "Arimo",Arial,sans-serif;color:#222;text-align:center;white-space:nowrap}
.remember{left:56px;top:168px;display:flex;align-items:center;gap:6px;font:400 13px/1 "Arimo",Arial,sans-serif;color:#222;white-space:nowrap}
.remember i{width:13px;height:13px;background:#fff;border:1px solid #777;border-radius:2px}
.forgot{left:0;top:194px;width:287px;text-align:center;font:400 13.5px/1 "Arimo",Arial,sans-serif;color:#222}

/* footer */
.site-footer{left:0;top:899px;width:1091px;height:301px;background:linear-gradient(#3a3a3a,#2e2e2e 85%,#242424)}
.footer-title{font:400 19px/1 "Open Sans",sans-serif;color:#e2e2e2;letter-spacing:.5px;text-transform:uppercase}
.address{left:59px;top:51px;font:400 14.5px/21px "Arimo",Arial,sans-serif;color:#f0f0f0}
.contact-box{left:55px;top:120px;width:340px;height:74px;background:#262626;border:1px solid #4a4a4a;border-radius:3px;padding:5px 7px;display:grid;grid-template-columns:116px 1fr;font:400 14.5px/21.5px "Arimo",Arial,sans-serif;color:#f2f2f2;white-space:nowrap}
.contact-box dt{letter-spacing:.6px}
.contact-box dd{font-weight:700}
.direction-btn{left:55px;width:268px;height:36px;background:#262626;font:400 14.5px/36px "Arimo",Arial,sans-serif;color:#f0f0f0;padding-left:6px;white-space:nowrap}
.direction-btn svg{position:absolute;right:8px;top:12px}
.social{width:42px;height:44px;border-radius:50%}
.social.one{left:471px;top:48px;background:radial-gradient(circle at 40% 30%,#7fd3f7,#1f8fd0 70%)}
.social.two{left:533px;top:47px;width:46px;height:46px;background:radial-gradient(circle at 40% 30%,#5c7fc4,#1f3c82 70%)}
.badge{border:1px solid var(--yellow)}
.copyright{left:753px;top:273px;font:400 11px/1 "Arimo",Arial,sans-serif;color:#f0f0f0;white-space:nowrap}
</style>
</head>
<body>

<header class="site-header abs">
  <div class="date-badge abs">7 February 2012</div>
  <div class="brand abs"><span class="brand-mark"></span>Brindle Haulage</div>
  <nav class="main-nav abs">
    <a class="current" href="#">HOME</a>
    <a href="#">INTRODUCTION</a>
    <a href="#">CULTURE</a>
    <a href="#">THE TEAM</a>
    <a href="#">DEPOTS</a>
    <a href="#">NOTICE BOARD</a>
    <a href="#">CUSTOMER FEEDBACK</a>
    <a href="#">CONTACT</a>
  </nav>
</header>

<section class="hero abs">
  <div class="hero-glow abs"></div>
  <div class="hero-photo abs" role="img" aria-label="Photograph of a dark curtain-sided lorry trailer driving along a motorway lane beside a crash barrier and grass verge"></div>
  <div class="slide-dots abs"><span class="active"></span><span></span><span></span><span></span></div>
  <h1 class="hero-title abs">Road Hauliers<br>and Distribution<br>Specialist</h1>
  <p class="hero-services abs">Part Loads, Full Loads<br>Abnormal Loads<br>Long, High, Wide</p>
  <p class="hero-slogan abs">We can move IT</p>
</section>

<main class="content abs">
  <h2 class="intro-title abs">Introduction</h2>
  <div class="intro-rule abs"></div>
  <p class="intro-text abs">Brindle Haulage (Midlands) Ltd we are a family owned and run Transport and Distribution company. We believe that by developing our staff through Talent Partners and an ongoing driver assessment program we can maintain a leading edge with in the market place. Brindle Haulage operate over sixty vehicles throughout the Black Country, some of which are based in our customer premises and are painted in their livery.</p>
  <div class="callout abs">We can arrange all documention, inc. movement orders and support vehicals</div>

  <aside class="login abs">
    <div class="login-head abs">CUSTOMER LOGIN</div>
    <div class="login-body abs">
      <span class="field-label abs" style="top:34px">Username</span>
      <div class="field abs" style="top:26px"></div>
      <span class="field-label abs" style="top:73px">Password</span>
      <div class="field abs" style="top:64px"></div>
      <div class="btn abs" style="left:20px;top:114px;width:134px">Create new user</div>
      <div class="btn abs" style="left:170px;top:114px;width:82px">Login</div>
      <div class="remember abs"><i></i>Remember my login details</div>
      <div class="forgot abs">Forgot login details. Click here</div>
    </div>
  </aside>
</main>

<footer class="site-footer abs">
  <h3 class="footer-title abs" style="left:59px;top:19px">Contact Details</h3>
  <p class="address abs">Millbrook Yard, Old Forge Road,<br>Harden Cross, Nr Ashwell, Stourbridge,<br>DY9 4QT</p>
  <dl class="contact-box abs">
    <dt>TELEPHONE</dt><dd>01632 960466</dd>
    <dt>FAX</dt><dd>01632 960915</dd>
    <dt>E:MAIL</dt><dd>info@brindlehaulage.co.uk</dd>
  </dl>
  <a class="direction-btn abs" style="top:202px">Directions to Ashwell Depot
    <svg width="15" height="11" viewBox="0 0 15 11"><path d="M0 5.5h12M8 1l5 4.5L8 10" fill="none" stroke="#fdbf1f" stroke-width="2"/></svg></a>
  <a class="direction-btn abs" style="top:241px">Directions to Kelbrook Depot
    <svg width="15" height="11" viewBox="0 0 15 11"><path d="M0 5.5h12M8 1l5 4.5L8 10" fill="none" stroke="#fdbf1f" stroke-width="2"/></svg></a>

  <h3 class="footer-title abs" style="left:471px;top:19px">Follow Us</h3>
  <a class="social one abs" aria-label="Follow us on social network one"></a>
  <a class="social two abs" aria-label="Follow us on social network two"></a>

  <h3 class="footer-title abs" style="left:753px;top:20px">Membership</h3>
  <div class="badge abs" style="left:752px;top:61px;width:113px;height:79px;background:#0f3016" role="img" aria-label="Staff development accreditation badge"></div>
  <div class="badge abs" style="left:880px;top:68px;width:60px;height:51px;background:#fff;border-color:#ddd" role="img" aria-label="Freight trade association membership badge"></div>
  <div class="badge abs" style="left:960px;top:52px;width:69px;height:84px;background:#1c3a1c" role="img" aria-label="Trade guild membership badge"></div>

  <p class="copyright abs">Copyright 2012 Brindle Haulage.All rights reserved</p>
</footer>

</body>
</html>
```